Überarbeitung - Redesign der TRAVIOnet Website
die vorhandene Webseite www.travio-net.example mit dem Blog www.blog.travio-net.example soll komplett aufgesfrischt, neu gestaltet und gestrafft werden. Dabei fallen einige Texte weg. Insgesamt müssen aber texte überarbeitet werden. Ebenfalls ist noch eine Modernisierung des Logos angedacht.
Sorry leute, ist meine erste Auschreibung hier. Dass ich dafür nicht auch noch ein Logo und die Textüberarbeitung gekomme ist klar. Das sollte nur ein Hinweis sein, daß das auch noch zu machen ist. Selbstverständlich separat. Also hier geht es nur ums Design der Webseite!!

```html
<!DOCTYPE html>
<html lang="de">
<head>
<meta charset="utf-8">
<title>TRAVIOnet – Leistungsübersicht</title>
<link rel="stylesheet" href="https://fonts.googleapis.com/css2?family=Arimo:ital,wght@0,400;0,700;1,400&display=swap">
<style>
  :root {
    --page-bg: #eeeeee;
    --paper: #ffffff;
    --frame: #333333;
    --accent: #e3262b;
    --text: #1e1e1e;
    --muted: #6b6b6b;
    --nav: #555555;
    --soft: #b5b5b5;
    --footer-bg: #d2d3d5;
  }
  * { box-sizing: border-box; margin: 0; padding: 0; }
  html, body { width: 1200px; height: 690px; overflow: hidden; }
  body {
    background: var(--page-bg);
    font-family: "Arimo", Arial, sans-serif;
    color: var(--text);
    position: relative;
  }
  .page {
    position: absolute; left: 86px; top: 0; width: 1011px; height: 690px;
    background: var(--paper);
    border-left: 1px solid var(--frame);
    border-right: 1px solid var(--frame);
  }
  .rule {
    position: absolute; left: 246px; top: 12px; width: 4px; height: 678px;
    background: var(--accent);
  }
  .brand {
    position: absolute; left: 22px; top: 50px; width: 215px;
    display: flex; align-items: center; justify-content: flex-end; gap: 10px;
  }
  .brand-mark { width: 14px; height: 14px; background: var(--accent); }
  .brand-name { font-size: 28px; line-height: 1; color: var(--accent); white-space: nowrap; }
  .nav {
    position: absolute; left: 0; top: 160px; width: 237px;
    list-style: none; text-align: right;
  }
  .nav li { height: 28.7px; font-size: 14.5px; color: var(--nav); white-space: nowrap; }
  .nav .is-active { color: var(--accent); }
  .blog-link {
    position: absolute; right: 26px; top: 16px;
    display: flex; align-items: center; gap: 7px;
    font-size: 15px; color: var(--muted); white-space: nowrap;
  }
  .blog-link span { width: 10px; height: 10px; background: var(--accent); }
  .tagline {
    position: absolute; left: 260px; top: 105px;
    font-size: 19.5px; font-style: italic; color: var(--soft); white-space: nowrap;
  }
  .tagline em { color: var(--accent); }
  .hero { position: absolute; left: 250px; top: 141px; width: 760px; height: 269px; display: flex; }
  .hero-photo {
    width: 442px; height: 100%;
    background: linear-gradient(100deg, #c9c3b6 0%, #a89f90 40%, #6f6a62 75%, #4c4a47 100%);
  }
  .service {
    flex: 1; position: relative; border-left: 1px solid rgba(255,255,255,.35);
    background: linear-gradient(var(--top) 0 35px, var(--body) 35px);
  }
  .service span {
    position: absolute; left: 50%; bottom: 6px;
    writing-mode: vertical-rl; transform: translateX(-50%) rotate(180deg);
    color: #fff; font-size: 16px; white-space: nowrap; letter-spacing: .3px;
  }
  .section-title {
    position: absolute; left: 261px; top: 429px;
    font-size: 14.5px; font-weight: 400; color: var(--accent); white-space: nowrap;
  }
  .subnav {
    position: absolute; left: 430px; top: 428px; height: 64px;
    border-left: 1px solid var(--soft); padding-left: 5px;
    list-style: none; font-size: 13px; color: var(--nav); line-height: 23.4px;
  }
  .intro {
    position: absolute; left: 267px; top: 515px; width: 728px;
    font-size: 12.7px; line-height: 23.5px; color: var(--text);
  }
  .footer {
    position: absolute; left: 250px; top: 659px; width: 760px; height: 31px;
    background: var(--footer-bg); display: flex; gap: 22px; padding-left: 36px;
    align-items: center; font-size: 14px; color: var(--frame);
  }
</style>
</head>
<body>
  <div class="page">
    <div class="brand"><span class="brand-mark"></span><span class="brand-name">TRAVIOnet</span></div>
    <div class="rule"></div>
    <ul class="nav">
      <li>Home</li>
      <li class="is-active">Leistungsübersicht</li>
      <li>TRAVIO performance</li>
      <li>TRAVIO consulting</li>
      <li>TRAVIO coaching</li>
      <li>TRAVIO interim</li>
      <li>Referenzen</li>
      <li>Karriere</li>
      <li>Presse</li>
      <li>Team</li>
      <li>Kontakt</li>
    </ul>
    <div class="blog-link"><span></span>TRAVIO blog</div>
    <p class="tagline">Wir optimieren <em>Ihren Vertrieb</em> und steigern <em>Umsatz!</em></p>
    <div class="hero">
      <div class="hero-photo" role="img" aria-label="Foto: lächelnde Beraterin im Büro"></div>
      <div class="service" style="--top:#8a8470;--body:#5b594d"><span>TRAVIO Performance</span></div>
      <div class="service" style="--top:#8593a4;--body:#4b515b"><span>TRAVIO Consulting</span></div>
      <div class="service" style="--top:#7d736b;--body:#4f4b47"><span>TRAVIO Coaching</span></div>
      <div class="service" style="--top:#8f8f8f;--body:#555456"><span>TRAVIO Interim</span></div>
      <div class="service" style="--top:#958a7d;--body:#4e4a46"><span>TRAVIO recruit &amp; lead</span></div>
    </div>
    <h1 class="section-title">LEISTUNGSÜBERSICHT</h1>
    <ul class="subnav">
      <li>Analysieren</li>
      <li>Beraten</li>
      <li>Umsetzen</li>
    </ul>
    <p class="intro">Unsere langjährigen Vertriebserfahrungen in der IT, Telekommunikation und High Technologie, Consulting, Beauty, Health Care befähigen unsere Vertriebsprofis und Management Praktiker, Sie zu unterstützen, Ihre Entscheidungen zu treffen und diese dann gemeinsam umsetzen.</p>
    <div class="footer"><span>Impressum</span><span>AGB</span></div>
  </div>
</body>
</html>
```